Business Card for Musician

The company is called Tolvik Music Entertainment and i am the director (Priya Hallorin) . I would like a logo made along with a list of services i provide :

Rock Pop and Jazz Covers music for Weddings , Birthdays , Pubs, Bars and Restaurants

I provide Solo/Duo and Bands for these functions.

Another aspect is i teach guitar and do music workshops and compose music for television.

I want to go for something different than a photo of a guitar or singer..i like the idea of soundwaves and an ear. or ripples of sound like a music note (as a drop of water) and the sound rippling out..another idea is something with lighting (music lights) with different colours lighting up the name Tolvik..however im open to any ideas. Thanks

Target Market(s)

General Public, Music Agents, Venue Owners. English Speaking..adults from 25-50

Industry/Entity Type

Business

Font styles to use
Sans Serif

Colors

Designer to choose colors to be used in the design.

Requirements
Must have
• All the points about what i do...
Nice to have
• Logo could emphasize the TOL in Tolvik...
Should not have
• Not too busy please...Simple but gets the message across. NOthing obvious like a photo of a musician playing.

```html
<!DOCTYPE html>
<html lang="en">
<head>
<meta charset="UTF-8">
<title>Tolvik Music Entertainment – Business Card</title>
<link href="https://fonts.googleapis.com/css2?family=Arimo:wght@700&display=swap" rel="stylesheet">
<style>
  :root {
    --page: #ffffff;
    --card: #231f20;
    --ink: #ffffff;
  }
  html, body {
    margin: 0;
    padding: 0;
    width: 1200px;
    height: 1000px;
    overflow: hidden;
    background: var(--page);
  }
  .canvas {
    position: relative;
    width: 1200px;
    height: 1000px;
    font-family: "Arimo", Arial, sans-serif;
    font-weight: 700;
    color: var(--ink);
  }
  .business-card {
    position: absolute;
    left: 97px;
    top: 176px;
    width: 989px;
    height: 570px;
    background: var(--card);
    border-radius: 22px;
    overflow: hidden;
  }
  .company-name {
    position: absolute;
    left: 55px;
    top: 44px;
    margin: 0;
    font-size: 21px;
    line-height: 1;
    font-weight: 700;
  }
  .brand-wordmark {
    position: absolute;
    left: 26px;
    top: 250px;
    margin: 0;
    font-size: 150px;
    line-height: 1;
    letter-spacing: -2px;
    font-weight: 700;
  }
  .service-text {
    position: absolute;
    margin: 0;
    font-size: 21px;
    line-height: 29px;
    font-weight: 700;
  }
  .services-list { left: 612px; top: 132px; }
  .services-acts { left: 612px; top: 247px; }
  .services-teaching { left: 551px; top: 326px; }
</style>
</head>
<body>
<main class="canvas">
  <section class="business-card">
    <h1 class="company-name">Tolvik Music Entertainment</h1>
    <p class="brand-wordmark">Tolvik</p>
    <p class="service-text services-list">Rock, Pop and Jazz covers,<br>music for Weddings, Birthdays,<br>Pubs, Bars and Restaurants.</p>
    <p class="service-text services-acts">I provide Solo/Duo and Bands<br>for these functions.</p>
    <p class="service-text services-teaching">Another aspect is I teach guitar and<br>do music workshops and compose<br>music for television.</p>
  </section>
</main>
</body>
</html>
```